Flyer-Design für Neueröffnung feinKragen
Zielgruppe
Wir bieten Marken Hemden und Accessoires unter anderem von den Herstellern Faltenmeister, Lumira und Veltrano in unserem Ladengeschäft sowie online in unserem Shop.
Unsere Zielgruppe ist der anspruchsvolle Mann, gut gebildet, aufstrebend und modebewusst, das ist das typische Bild unserer Zielgruppe.
Kunden können von uns ein modisches Hemd in hervorragender Qualität und exzellentem Service erwarten.
Aufgabenstellung
Feiern Sie mit uns die
NEU ERÖFFNUNG
Endlich in Oberkochen Markenhemden in großer Auswahl.
Am Samstag, 01. April 09:00-16:00Uhr
20% auf Alles - kein Aprilscherz
www.feinKragen.de
(Texte könne auch verändert werden, außer die Fakten - Neueröffnung - Datum - 20% auf alles)

```html
<!DOCTYPE html>
<html lang="de">
<head>
<meta charset="utf-8">
<title>feinKragen – Neueröffnung Flyer</title>
<link rel="stylesheet" href="https://fonts.googleapis.com/css2?family=Bodoni+Moda:wght@600;700&family=Open+Sans:wght@400;600&display=swap">
<style>
  :root{
    --plum:#4b1b43;
    --plum-dark:#3a1334;
    --plum-light:#5b2553;
    --mauve:#cdb8c9;
    --mauve-ring:#4b1b43;
    --white:#ffffff;
    --stage:#e6e3df;
    --photo-a:#b9b7b0;
    --photo-b:#3b3a44;
    --shirts-a:#2a2d4a;
    --shirts-b:#7b2b3a;
    --serif:"Bodoni Moda", "Times New Roman", serif;
    --sans:"Open Sans", Arial, sans-serif;
  }
  *{box-sizing:border-box;margin:0;padding:0}
  html,body{width:1200px;height:800px;overflow:hidden;background:var(--stage)}
  .stage{position:relative;width:1200px;height:800px}
  .flyer{position:absolute;top:55px;width:500px;height:690px;overflow:hidden;
    background:linear-gradient(160deg,var(--plum-light),var(--plum) 45%,var(--plum-dark));
    box-shadow:0 6px 18px rgba(0,0,0,.25);color:var(--white)}
  .flyer--front{left:70px}
  .flyer--back{left:630px}
  .flyer__photo{position:absolute;inset:0;width:500px;height:690px}
  .seal{position:absolute;border-radius:50%;background:var(--mauve);color:var(--plum);
    display:flex;flex-direction:column;align-items:center;justify-content:center;text-align:center;
    box-shadow:0 4px 10px rgba(0,0,0,.35)}
  .seal::before{content:"";position:absolute;inset:7px;border-radius:50%;border:1.5px solid var(--mauve-ring)}
  .seal--offer{left:73px;top:168px;width:124px;height:124px;transform:rotate(-10deg)}
  .seal__small{font-family:var(--sans);font-size:11px}
  .seal__big{font-family:var(--serif);font-weight:700;font-size:44px;line-height:1}
  .seal--party{left:57px;top:343px;width:136px;height:136px;transform:rotate(-8deg)}
  .seal__party-text{font-family:var(--sans);font-size:19px;line-height:1.25}
  .bar{position:absolute;background:var(--white);height:6px}
  .rule{position:absolute;background:var(--white);height:1px}
  .kicker{position:absolute;font-family:var(--sans);font-size:13px;left:0;right:0;text-align:center}
  .headline{position:absolute;left:0;right:0;top:326px;text-align:center;font-family:var(--serif);font-weight:700;font-size:44px;letter-spacing:1px}
  .subline{position:absolute;left:0;right:0;text-align:center;font-family:var(--sans)}
  .brands{position:absolute;left:30px;right:30px;top:450px;display:flex;gap:8px;justify-content:center}
  .brand{background:var(--white);color:var(--plum);font-family:var(--sans);font-weight:600;font-size:12px;
    height:38px;padding:0 10px;display:flex;align-items:center;border:1px solid #ddd}
  .date{position:absolute;left:0;right:0;top:500px;text-align:center;font-family:var(--sans);font-size:25px}
  .band{position:absolute;left:0;right:0;top:555px;height:72px;background:var(--white);
    display:flex;align-items:center;justify-content:center;gap:14px}
  .brandmark__dot{width:46px;height:46px;border-radius:50%;background:var(--plum)}
  .brandmark__name{font-family:var(--serif);font-weight:700;font-size:46px;color:var(--plum);letter-spacing:4px}
  .url{position:absolute;left:0;right:0;top:642px;text-align:center;font-family:var(--sans);font-size:22px}
  .location{position:absolute;left:30px;top:278px;width:180px;text-align:center;font-family:var(--sans);font-size:17px;line-height:1.35;text-transform:uppercase}
  .benefits{position:absolute;left:225px;top:292px;width:250px;list-style:none}
  .benefit{font-family:var(--serif);font-weight:600;font-size:17px;line-height:1.2;padding-bottom:6px;border-bottom:1px solid var(--white);margin-bottom:20px;position:relative}
  .benefit::after{content:"";position:absolute;left:0;right:20px;bottom:-11px;height:5px;background:var(--white)}
</style>
</head>
<body>
<main class="stage">

  <section class="flyer flyer--front">
    <svg class="flyer__photo" viewBox="0 0 500 690" role="img" aria-label="Foto eines jungen Mannes in dunklem Sakko und weißem Hemd vor heller Wand">
      <defs>
        <linearGradient id="portrait" x1="0" y1="0" x2="0" y2="1">
          <stop offset="0" stop-color="var(--photo-a)"/>
          <stop offset="1" stop-color="var(--photo-b)"/>
        </linearGradient>
      </defs>
      <polygon points="0,0 500,0 240,275" fill="url(#portrait)"/>
    </svg>

    <div class="seal seal--offer">
      <span class="seal__small">Auf alles</span>
      <span class="seal__big">20%</span>
      <span class="seal__small">...kein Aprilscherz</span>
    </div>

    <p class="kicker" style="top:298px">Feiern Sie mit uns die</p>
    <div class="bar" style="top:318px;left:70px;right:40px"></div>
    <div class="rule" style="top:325px;left:40px;right:40px"></div>
    <h1 class="headline">NEU ERÖFFNUNG</h1>
    <div class="rule" style="top:382px;left:40px;right:40px"></div>
    <div class="bar" style="top:390px;left:40px;right:60px"></div>

    <p class="subline" style="top:403px;font-size:17px">Endlich in Oberkochen</p>
    <p class="subline" style="top:427px;font-size:11px">Markenhemden in großer Auswahl...</p>

    <div class="brands">
      <span class="brand">Faltenmeister</span>
      <span class="brand">Lumira</span>
      <span class="brand">Veltrano</span>
      <span class="brand">Marvello</span>
      <span class="brand">Brennholt</span>
    </div>

    <p class="date">Samstag, 01. April 09:00-16:00 Uhr</p>

    <div class="band">
      <span class="brandmark__dot"></span>
      <span class="brandmark__name">feinKragen</span>
    </div>
    <p class="url">www.feinKragen.de</p>
  </section>

  <section class="flyer flyer--back">
    <svg class="flyer__photo" viewBox="0 0 500 690" role="img" aria-label="Foto gestapelter karierter Hemden mit Ledergürtel auf Holz">
      <defs>
        <linearGradient id="shirts" x1="0" y1="0" x2="1" y2="1">
          <stop offset="0" stop-color="var(--shirts-a)"/>
          <stop offset="1" stop-color="var(--shirts-b)"/>
        </linearGradient>
      </defs>
      <polygon points="0,0 500,0 225,290" fill="url(#shirts)"/>
    </svg>

    <p class="location">Jetzt in<br>Oberkochen</p>

    <div class="seal seal--party">
      <span class="seal__party-text">Feiern Sie<br>mit uns!</span>
    </div>

    <ul class="benefits">
      <li class="benefit">Marken Hemden</li>
      <li class="benefit">Accessoires</li>
      <li class="benefit">modische Hemden in hervorragender Qualität</li>
      <li class="benefit">exzellenter Service</li>
    </ul>

    <div class="band">
      <span class="brandmark__dot"></span>
      <span class="brandmark__name">feinKragen</span>
    </div>
    <p class="url">www.feinKragen.de</p>
  </section>

</main>
</body>
</html>
```